Hip Music Management Co. BIz Card

I have a logo (attached) the back side of the card should the full logo on the entire card- that's it. The front side of the card should show the logo somewhere, keeping with the 4 different shades of blue. The front side of the card can be a white background with logo and colored typeface for all info. Pretty simple.

Target Market(s)

I manage and produce a whole bunch of major label and indie artists.

Industry/Entity Type

Management

Contact Information for Business Card

Velmora Sound House (logo)
Dale Fornwick
President
www.velmorasoundhouse.com
dale@velmorasoundhouse.com
+1 310.555.7182
418 Willow Bend Lane
Ashgrove Falls, NY 10599

Requirements
Must have
• Entire logo on back side. White background on front- unless you provide something more interesting.
Nice to have
• On the front of the card if you choose a white backgound, if possible take my logo without the blue background (over white) that would be cool.

```html
<!DOCTYPE html>
<html lang="en">
<head>
<meta charset="utf-8">
<title>Velmora Sound House – Business Card</title>
<link rel="stylesheet" href="https://fonts.googleapis.com/css2?family=Open+Sans:wght@400;600;700&display=swap">
<style>
  :root {
    --backdrop: #e9ebef;
    --card-white: #ffffff;
    --navy: #18244f;
    --navy-glow: #3a4370;
    --teal: #16a8c2;
    --sky: #4aa6de;
    --steel: #1c5f93;
    --ink: #1d2a4e;
    --link: #1a6aa6;
  }
  * { box-sizing: border-box; margin: 0; padding: 0; }
  html, body { width: 1200px; height: 731px; overflow: hidden; }
  body {
    background: var(--backdrop);
    font-family: "Open Sans", sans-serif;
    display: flex;
    align-items: center;
    justify-content: center;
    gap: 60px;
  }
  .card {
    width: 520px;
    height: 297px;
    position: relative;
    box-shadow: 0 6px 18px rgba(0,0,0,0.18);
  }
  .card--front { background: var(--card-white); }
  .brand-name {
    position: absolute;
    left: 26px;
    top: 26px;
    font-size: 21px;
    font-weight: 700;
    color: var(--teal);
    line-height: 1.1;
  }
  .person {
    position: absolute;
    left: 26px;
    top: 80px;
  }
  .person__name { font-size: 17px; font-weight: 700; color: var(--ink); }
  .person__title { font-size: 14px; color: var(--ink); margin-top: 2px; }
  .address {
    position: absolute;
    right: 26px;
    top: 24px;
    text-align: right;
    font-size: 19px;
    line-height: 1.1;
    color: var(--steel);
  }
  .contact {
    position: absolute;
    left: 26px;
    bottom: 22px;
    font-size: 15px;
    line-height: 1.55;
    color: var(--link);
  }
  .card--back {
    background: radial-gradient(ellipse 62% 48% at 50% 50%, var(--navy-glow) 0%, var(--navy) 100%);
    display: flex;
    align-items: center;
    justify-content: center;
  }
  .back-brand {
    font-size: 36px;
    font-weight: 700;
    color: var(--sky);
    letter-spacing: 0.5px;
  }
</style>
</head>
<body>
  <section class="card card--front" aria-label="Card front">
    <div class="brand-name">Velmora Sound House</div>
    <div class="person">
      <div class="person__name">Dale Fornwick</div>
      <div class="person__title">President</div>
    </div>
    <div class="address">
      Willow Bend Lane<br>
      Ashgrove Falls<br>
      NY 10599
    </div>
    <div class="contact">
      <div>+1 310.555.7182 418</div>
      <div>www.velmorasoundhouse.com</div>
      <div>dale@velmorasoundhouse.com</div>
    </div>
  </section>
  <section class="card card--back" aria-label="Card back">
    <div class="back-brand">Velmora Sound House</div>
  </section>
</body>
</html>
```